Velvet & Vine by Mona
Text 410.582.3174 to set up and appointment
Instagram is Velvet_VineByMona
Location 4182 Carrow Ln. Notthingham Md, 21094 Suit 204
Slogan "Polished Looks. Radiant Days.
Specializing in pressicion cuts, blonding, fades, perms, waxing and more

The salon is black, gun metal color mirror with led lights. Green plants and has natural wood countertops for accent colors. Modern yet elegant. I want the card simple but it needs something to really grab the clients attention. I like black, grey, gold, green, natural tones and hints of pink or gold coloring
I’m open to anything. I don’t have a logo. Suggestions are welcome

Target Market(s)

20-60 men and woman

Industry/Entity Type

Hairstylist / barber

The name of the show should be bold. Maybe the letters could raised I also like foil for shine added or a mat finish

Colors

Requirements
Must have
• I also like some floral Floral designs, but not too overpowering. I like Sparkle, Watercolor design, Or a geometric line in the background
Nice to have
• I’m really here because I need creative help. I’m open for suggestions. I’ll post a picture of the salon in inspiration if I can find it.
Should not have
• Checkered background

```html
<!DOCTYPE html>
<html lang="en">
<head>
<meta charset="utf-8">
<title>Velvet &amp; Vine by Mona — Business Card</title>
<link rel="stylesheet" href="https://fonts.googleapis.com/css2?family=Alex+Brush&family=Montserrat:wght@500;600&display=swap">
<style>
  :root {
    --plum: #4e1450;
    --magenta: #b4307f;
    --rose: #c46f8c;
    --sage: #a69c6c;
    --leaf: #65a844;
    --cream: #f4eeb4;
    --cream-text: #f7f1d0;
    --petal-light: #f0c8ee;
    --petal-deep: #b35aa8;
  }
  html, body {
    margin: 0;
    padding: 0;
    width: 1200px;
    height: 674px;
    overflow: hidden;
    background: #2a2a2a;
  }
  .card {
    position: relative;
    width: 1200px;
    height: 674px;
    overflow: hidden;
    background: linear-gradient(180deg,
      var(--plum) 0%,
      #7a1e6e 18%,
      var(--magenta) 42%,
      var(--rose) 62%,
      var(--sage) 80%,
      var(--leaf) 100%);
    font-family: "Montserrat", sans-serif;
    color: var(--cream-text);
  }
  .card-frame,
  .sparkles {
    position: absolute;
    inset: 0;
  }
  .flower-art {
    position: absolute;
    top: -40px;
    right: -50px;
    width: 300px;
    height: 320px;
    border-radius: 50%;
    background: radial-gradient(circle at 50% 42%,
      #f3dcf2 0%, var(--petal-light) 18%, #dc9ad6 45%, var(--petal-deep) 75%, rgba(179,90,168,0) 100%);
  }
  .brand-badge {
    position: absolute;
    left: 538px;
    top: 71px;
    width: 122px;
    height: 122px;
    border: 3px solid var(--cream);
    border-radius: 50%;
    display: flex;
    align-items: center;
    justify-content: center;
    text-align: center;
    box-sizing: border-box;
  }
  .brand-badge span {
    font-size: 19px;
    font-weight: 600;
    line-height: 1.15;
    letter-spacing: 1px;
    color: var(--cream);
  }
  .script {
    position: absolute;
    left: 0;
    width: 100%;
    text-align: center;
    font-family: "Alex Brush", cursive;
    color: var(--cream);
    text-shadow: 1px 2px 2px rgba(60, 20, 40, 0.55), -1px -1px 0 rgba(255, 255, 230, 0.35);
    margin: 0;
    font-weight: 400;
  }
  .business-name {
    top: 198px;
    font-size: 76px;
    line-height: 1;
  }
  .business-name .by-line {
    display: block;
    font-size: 64px;
    margin-top: -6px;
    margin-left: -20px;
  }
  .tagline {
    position: absolute;
    top: 366px;
    left: 0;
    width: 100%;
    text-align: center;
    font-size: 23px;
    font-weight: 500;
    letter-spacing: 1.2px;
    margin: 0;
  }
  .contact-icon {
    position: absolute;
    left: 576px;
    top: 414px;
    width: 52px;
    height: 52px;
  }
  .stylist-name {
    top: 468px;
    font-size: 56px;
  }
  .contact-list {
    position: absolute;
    top: 545px;
    left: 0;
    width: 100%;
    margin: 0;
    padding: 0;
    list-style: none;
    text-align: center;
    font-size: 17px;
    font-weight: 500;
    letter-spacing: 1.3px;
    line-height: 29px;
  }
</style>
</head>
<body>
<main class="card">
  <svg class="card-frame" width="1200" height="674" viewBox="0 0 1200 674" aria-hidden="true">
    <path d="M960 16 H14 V659 H1186 V316" fill="none" stroke="var(--cream)" stroke-width="2"/>
  </svg>

  <div class="flower-art" role="img" aria-label="Pink dahlia flower illustration in the top right corner"></div>

  <svg class="sparkles" width="1200" height="674" viewBox="0 0 1200 674" aria-hidden="true">
    <defs>
      <path id="sparkle" d="M0 -1 Q0.12 -0.12 1 0 Q0.12 0.12 0 1 Q-0.12 0.12 -1 0 Q-0.12 -0.12 0 -1Z"/>
    </defs>
    <g fill="var(--cream)">
      <use href="#sparkle" transform="translate(941 45) scale(14)"/>
      <use href="#sparkle" transform="translate(951 119) scale(14)"/>
      <use href="#sparkle" transform="translate(978 184) scale(14)"/>
      <use href="#sparkle" transform="translate(1040 246) scale(14)"/>
      <use href="#sparkle" transform="translate(1118 276) scale(14)"/>
      <use href="#sparkle" transform="translate(1136 615) scale(28)"/>
      <use href="#sparkle" transform="translate(1112 586) scale(14)"/>
      <use href="#sparkle" transform="translate(1151 575) scale(10)"/>
    </g>
  </svg>

  <div class="brand-badge"><span>VELVET<br>&amp; VINE</span></div>

  <h1 class="script business-name">Velvet &amp; Vine<span class="by-line">by Mona</span></h1>

  <p class="tagline">“Specializing in pressicion cuts, blonding, fades, perms, waxing and more”</p>

  <svg class="contact-icon" viewBox="0 0 52 52" aria-hidden="true">
    <circle cx="26" cy="26" r="24" fill="none" stroke="var(--cream)" stroke-width="2.5"/>
    <circle cx="26" cy="19" r="7.5" fill="var(--cream)"/>
    <path d="M12 39 Q12 28 26 28 Q40 28 40 39 Z" fill="var(--cream)"/>
  </svg>

  <h2 class="script stylist-name">Mona Ellery</h2>

  <ul class="contact-list">
    <li>Text: 410.582.3174 to set up and appointment</li>
    <li>Instagram: @Velvet_VineByMona</li>
    <li>Location: 4182 Carrow Ln. Notthingham Md, 21094 Suit 204</li>
  </ul>
</main>
</body>
</html>
```